Keystone Vault Depot Services Needs A Website

We are looking for a website for a new company. 4 Pages

Needs to be responsive and mobile friendly for all browsers and coded for both Android & IOS. SEO is also important.

Website Brief – Keystone Vault Depot Services
Domain: www.keystonevaultdepot.com
Email: info@keystonevaultdepot.com
Phone: to be inserted later
Address: 10458 82 Ave, Edmonton, AB T6E 2K9
Platform: WordPress (recommended for flexibility, SEO tools, and ease of editing)
Requirements:
• Responsive & mobile-friendly (Android & iOS)
• Cross-browser compatibility
• Fast page load speed
• SEO optimized for storage development, management, and investment keywords
• Easy in-house editing after launch
• Professional, modern, trust-driven design reflecting expertise, reliability, and innovation
________________________________________
Pages
1. HOME
Purpose: Quickly communicate who Keystone Vault Depot Services is and why they’re the best choice for designing, building, leasing, and managing self storage facilities.
Content Highlights:
• Hero Section: Large, bold image of a modern self storage facility with headline:
"From Concept to Capacity – Your Self Storage Experts"
• Subheadline: “Keystone Vault Depot Services delivers turnkey design, construction, leasing, and management services for profitable self storage operations.”
• Quick Service Icons:
o Facility Design & Development
o Construction & Build Management
o Lease-Up & Marketing
o Ongoing Facility Management
• Call to Action Button: “LEARN MORE” → links to ABOUT US page.
• Featured Project Highlights: Showcase a few completed or current projects with photos and stats.
• Contact Banner: “Ready to build your next self storage project? Let’s talk.” → CONTACT page.
2. ABOUT US
Purpose: Build credibility, showcase experience, and explain the value proposition.
Content Highlights:
• Who We Are: Overview of Keystone Vault Depot Services’ history, mission, and team expertise.
• Our Approach: End-to-end process from site selection to occupancy.
• Why Choose Us:
o Industry expertise in self storage
o Proven track record in lease-up success
o Strong vendor and contractor network
3. SERVICES
Purpose: Detail all service offerings with clarity and authority.
Sections:
• Design & Development: Market analysis, site planning, and architectural design.
• Construction Management: Overseeing timelines, budgets, and quality control.
• Lease-Up Strategy: Marketing, promotions, and occupancy acceleration.
• Ongoing Facility Management: Staffing, maintenance, revenue optimization.

4. CONTACT
Purpose: Provide simple, direct ways to connect.
Content Highlights:
• Contact Form (Name, Email, Phone, Message)
• Direct Email: info@keystonevaultdepot.com
• Phone (if applicable)
• Google Map embed (if there’s a head office location)
• CTA: “Let’s Build Your Storage Success Story.”
Design & Technical Notes
• Visual Style: Clean, modern, bold typography, professional color palette (to be based on branding), strong imagery of self storage facilities.
• Performance: Image compression, caching, responsive scaling.
• SEO Targets: “Self storage facility developer,” “self storage construction,” “self storage management company,” “lease-up services for self storage.”

WordPress or Joomla – must be desktop and mobile friendly with fast page load speed. Need the ability to edit ourselves.

Use pantone colours - #033c5a – dark blue
#2baadf – light blue

```html
<!DOCTYPE html>
<html lang="en">
<head>
<meta charset="utf-8">
<title>Keystone Vault Depot Services – Self Storage Experts</title>
<link rel="stylesheet" href="https://fonts.googleapis.com/css2?family=Bebas+Neue&family=Lexend:wght@500;600;700&family=Poppins:wght@400;500;600&display=swap">
<style>
:root{
  --dark:#033c5a;
  --light:#2baadf;
  --ink:#1d2a33;
  --white:#ffffff;
  --hero-dark:#1b1d20;
}
*{box-sizing:border-box;margin:0;padding:0}
html,body{width:1200px;height:4187px;overflow:hidden}
body{position:relative;background:var(--white);font-family:"Poppins",sans-serif;color:var(--ink)}
.abs{position:absolute}

/* header */
.site-header{position:absolute;left:0;top:0;width:1200px;height:115px;background:var(--white)}
.brand{left:65px;top:36px;display:flex;align-items:center;gap:10px}
.brand-mark{width:34px;height:34px;background:var(--dark)}
.brand-name{font-family:"Lexend",sans-serif;font-weight:600;font-size:17px;color:var(--dark);line-height:1.15;width:170px}
.nav{top:50px;font-size:15px;font-weight:500;color:var(--dark);letter-spacing:.3px}
.btn-top{left:964px;top:35px;width:166px;height:47px;background:var(--light);color:var(--white);font-size:15px;display:flex;align-items:center;justify-content:center}

/* hero */
.hero{left:0;top:115px;width:1200px;height:930px}
.hero-title{left:0;width:1200px;text-align:center;font-family:"Bebas Neue",sans-serif;font-size:88px;line-height:1}
.hero-sub{left:0;top:786px;width:1200px;text-align:center;color:var(--white);font-size:20px;line-height:25px;font-weight:500}
.btn-arrow{display:flex;align-items:center;gap:14px;padding-left:24px;color:var(--white);clip-path:polygon(0 0,88% 0,100% 50%,88% 100%,0 100%)}
.hero-btn{left:514px;top:873px;width:228px;height:67px;background:var(--light);font-size:22px}

/* section titles */
.sec-title{left:0;width:1200px;text-align:center;font-family:"Lexend",sans-serif;font-weight:600;font-size:48px;color:var(--dark);letter-spacing:-1px}
.sec-kicker{left:0;width:1200px;text-align:center;font-family:"Lexend",sans-serif;font-weight:500;font-size:19px;color:var(--light)}
.sec-kicker span::before,.sec-kicker span::after{content:"";display:inline-block;width:46px;height:2px;background:var(--light);vertical-align:middle;margin:0 8px}

/* services */
.service-graphic{left:410px;top:1295px;width:380px;height:325px;background:linear-gradient(135deg,var(--dark),var(--light));clip-path:polygon(50% 0,100% 26%,100% 62%,52% 100%,2% 82%,0 26%)}
.diamond{width:80px;height:80px;transform:rotate(45deg);border:3px solid var(--white);outline:2px solid currentColor}
.diamond.dark{background:var(--dark);color:var(--dark)}
.diamond.light{background:var(--light);color:var(--light)}
.service-label{font-size:21px;line-height:24px;color:var(--ink)}

/* about */
.about-photo{left:50px;top:1752px;width:470px;height:420px;background:linear-gradient(180deg,#c9cbcd,#b98f5a 60%,#2b2b2b);clip-path:polygon(50% 0,100% 22%,100% 78%,50% 100%,0 78%,0 22%);outline:none}
.about-frame{left:50px;top:1752px;width:470px;height:420px;background:var(--light);clip-path:polygon(50% 0,100% 22%,100% 78%,50% 100%,0 78%,0 22%,2.5% 23.5%,2.5% 76.5%,50% 97%,97.5% 76.5%,97.5% 23.5%,50% 3%,2.5% 23.5%,0 22%)}
.about-badge{left:405px;top:2004px;width:200px;height:182px;background:var(--dark);clip-path:polygon(50% 0,100% 25%,100% 75%,50% 100%,0 75%,0 25%)}
.about-title{left:683px;top:1810px;font-family:"Lexend",sans-serif;font-weight:600;font-size:48px;color:var(--dark)}
.about-kicker{left:683px;top:1872px;font-family:"Lexend",sans-serif;font-weight:500;font-size:19px;color:var(--light)}
.about-kicker::after{content:"";display:inline-block;width:46px;height:2px;background:var(--light);vertical-align:middle;margin-left:8px}
.about-text{left:686px;top:1920px;width:442px;font-size:12.6px;line-height:24px;text-align:justify}
.about-btn{left:690px;top:2117px;width:167px;height:48px;background:var(--light);font-size:15px}

/* projects */
.project{overflow:hidden}
.project .photo{width:100%;height:100%}
.project .caption{position:absolute;left:30px;bottom:14px;color:var(--white);font-size:17px}
.project .arrow{position:absolute;right:16px;bottom:16px;width:20px;height:16px}
.dots{left:575px;top:3012px;display:flex;gap:8px}
.dots i{width:7px;height:7px;border:1.5px solid var(--dark);transform:rotate(45deg)}
.dots i.on{background:var(--dark)}

/* cta */
.cta-bg{left:0;top:2900px;width:1200px;height:900px;background:linear-gradient(180deg,#ffffff 0%,#b8dff0 22%,#5fbde4 55%,#3aa8d8 100%)}
.cta-title{left:0;top:3298px;width:1200px;text-align:center;font-family:"Lexend",sans-serif;font-weight:700;font-size:64px;line-height:78px;color:var(--white)}
.cta-sub{left:0;top:3486px;width:1200px;text-align:center;font-size:40px;color:var(--white)}
.cta-btn{left:457px;top:3582px;width:286px;height:78px;background:var(--dark);font-size:28px}

/* footer */
.footer-head{font-family:"Lexend",sans-serif;font-weight:500;font-size:20px;color:var(--light)}
.footer-head::after{content:"";display:block;width:40px;height:2px;background:var(--light);margin-top:10px}
.links{list-style:none;font-size:14px;color:var(--white)}
.links li{height:32px;display:flex;align-items:center;gap:12px}
.links li::before{content:"";width:12px;height:10px;background:var(--light);clip-path:polygon(50% 0,100% 35%,100% 100%,0 100%,0 35%)}
.footer-brand{left:470px;top:3960px;width:260px;text-align:center;font-family:"Lexend",sans-serif;font-weight:600;font-size:30px;line-height:34px;color:var(--white)}
.footer-mark{left:578px;top:3880px;width:44px;height:44px;background:var(--light)}
.contact-row{display:flex;gap:14px;color:var(--white);font-size:13px;line-height:16px;height:52px}
.contact-row .ico{width:28px;height:28px;border:1.5px solid var(--light);display:flex;align-items:center;justify-content:center;flex:none}
.rule{left:46px;top:4107px;width:1068px;height:1px;background:rgba(255,255,255,.25)}
.copy{left:0;top:4143px;width:1200px;text-align:center;font-size:12px;color:var(--white)}
</style>
</head>
<body>

<header class="site-header">
  <div class="abs brand"><span class="brand-mark"></span><span class="brand-name">Keystone Vault Depot Services</span></div>
  <a class="abs nav" style="left:378px">HOME</a>
  <a class="abs nav" style="left:478px">ABOUT US</a>
  <a class="abs nav" style="left:611px">SERVICES</a>
  <a class="abs nav" style="left:739px">FEATURED PROJECTS</a>
  <a class="abs btn-top">CONTACT US</a>
</header>

<section class="abs hero">
  <svg width="1200" height="930" class="abs" style="left:0;top:0">
    <defs>
      <linearGradient id="heroFill" x1="0" y1="0" x2="0" y2="1">
        <stop offset="0" stop-color="#2a2c2f"/>
        <stop offset=".35" stop-color="#8b8d90"/>
        <stop offset=".6" stop-color="#4a4c4f"/>
        <stop offset="1" stop-color="#17191b"/>
      </linearGradient>
    </defs>
    <g role="img" aria-label="Interior of a modern self storage warehouse with roll-up door and stacked boxes">
      <polygon points="0,0 1200,0 1200,760 600,925 0,760" fill="url(#heroFill)"/>
    </g>
    <polygon points="0,772 600,925 1200,772 1200,785 600,930 0,785" fill="var(--light)"/>
    <polygon points="0,760 600,915 1200,760 1200,772 600,925 0,772" fill="var(--hero-dark)"/>
  </svg>
  <div class="abs hero-title" style="top:490px;color:var(--white)">FROM CONCEPT TO CAPACITY</div>
  <div class="abs hero-title" style="top:570px;color:var(--light)">YOUR SELF STORAGE EXPERTS</div>
  <p class="abs hero-sub" style="top:672px">Keystone Vault Depot Services delivers turnkey design, construction, leasing,<br>and management services for profitable self storage operations.</p>
  <a class="abs btn-arrow hero-btn" style="top:758px">CONTACT US
    <svg width="26" height="20" viewBox="0 0 26 20"><path d="M2 7h12V2l10 8-10 8v-5H2z" fill="none" stroke="#fff" stroke-width="2"/></svg></a>
</section>

<h2 class="abs sec-title" style="top:1132px">OUR SERVICES</h2>
<div class="abs sec-kicker" style="top:1197px"><span>WHAT WE DO</span></div>

<div class="abs service-graphic" role="img" aria-label="Storage unit illustration with warehouse interior and keyhole door"></div>
<div class="abs service-label" style="left:90px;top:1365px;width:172px;text-align:right">Facility Design<br>&amp; Development</div>
<div class="abs diamond dark" style="left:293px;top:1347px"></div>
<div class="abs service-label" style="left:60px;top:1514px;width:204px;text-align:right">Construction &amp;<br>Build Management</div>
<div class="abs diamond light" style="left:293px;top:1494px"></div>
<div class="abs diamond light" style="left:832px;top:1347px"></div>
<div class="abs service-label" style="left:937px;top:1365px">Lease-Up &amp;<br>Marketing</div>
<div class="abs diamond dark" style="left:832px;top:1498px"></div>
<div class="abs service-label" style="left:940px;top:1514px">Ongoing Facility<br>Management</div>

<div class="abs about-photo" role="img" aria-label="Open storage unit filled with cardboard boxes"></div>
<div class="abs about-frame"></div>
<div class="abs about-badge"></div>
<h2 class="abs about-title">ABOUT US</h2>
<div class="abs about-kicker">WHO WE ARE</div>
<p class="abs about-text">Lorem ipsum dolor sit amet, consectetur adipiscing elit, sed do eiu smod tempor incididunt ut labore et dolore magna aliqua. Quis ipsum suspendisse ultrices gravida. Risus commodo viverra maec enas accumsan lacus vel facilisis.Lorem ipsum dolor sit amet, cons ectetur adipiscing elit, sed do eiusmod tempor incididunt ut labore et dolore magna aliqua. Quis ipsum suspendisse ultrices gravida. Risus commodo viverra maecenas accumsan lacus vel facilisis.</p>
<a class="abs btn-arrow about-btn">LEARN MORE
  <svg width="20" height="16" viewBox="0 0 26 20"><path d="M2 7h12V2l10 8-10 8v-5H2z" fill="none" stroke="#fff" stroke-width="2"/></svg></a>

<div class="cta-bg abs"></div>

<h2 class="abs sec-title" style="top:2362px">FEATURED PROJECT</h2>
<div class="abs sec-kicker" style="top:2428px"><span>PROJECT PORTFOLIO</span></div>

<div class="abs project" style="left:91px;top:2550px;width:310px;height:190px">
  <div class="photo" role="img" aria-label="Storage facility corridor with roll-up doors" style="background:linear-gradient(180deg,#d8dcdf,#8c99a4 55%,#0c3a56)"></div>
  <span class="caption">Lorem Ipsum Dolor</span>
  <svg class="arrow" viewBox="0 0 26 20"><path d="M2 7h12V2l10 8-10 8v-5H2z" fill="none" stroke="#fff" stroke-width="2"/></svg></div>
<div class="abs project" style="left:91px;top:2750px;width:310px;height:190px">
  <div class="photo" role="img" aria-label="Roll-up storage door with boxes" style="background:linear-gradient(180deg,#c9cdd0,#8d9aa3 55%,#0c3a56)"></div>
  <span class="caption">Lorem Ipsum Dolor</span>
  <svg class="arrow" viewBox="0 0 26 20"><path d="M2 7h12V2l10 8-10 8v-5H2z" fill="none" stroke="#fff" stroke-width="2"/></svg></div>
<div class="abs project" style="left:415px;top:2550px;width:374px;height:390px">
  <div class="photo" role="img" aria-label="Warehouse aisle with tall pallet racks" style="background:linear-gradient(180deg,#5a5a52,#a59a80 50%,#1a4660 85%,#0c3a56)"></div>
  <span class="caption">Lorem Ipsum Dolor Sit Aet</span>
  <svg class="arrow" viewBox="0 0 26 20"><path d="M2 7h12V2l10 8-10 8v-5H2z" fill="none" stroke="#fff" stroke-width="2"/></svg></div>
<div class="abs project" style="left:802px;top:2550px;width:310px;height:190px">
  <div class="photo" role="img" aria-label="Indoor storage hallway with green doors" style="background:linear-gradient(180deg,#d5dad6,#8fa3a6 55%,#0c3a56)"></div>
  <span class="caption">Lorem Ipsum Dolor</span>
  <svg class="arrow" viewBox="0 0 26 20"><path d="M2 7h12V2l10 8-10 8v-5H2z" fill="none" stroke="#fff" stroke-width="2"/></svg></div>
<div class="abs project" style="left:802px;top:2750px;width:310px;height:190px">
  <div class="photo" role="img" aria-label="Large warehouse floor with blue racking" style="background:linear-gradient(180deg,#4a6f96,#b8b394 50%,#0c3a56)"></div>
  <span class="caption">Lorem Ipsum Dolor</span>
  <svg class="arrow" viewBox="0 0 26 20"><path d="M2 7h12V2l10 8-10 8v-5H2z" fill="none" stroke="#fff" stroke-width="2"/></svg></div>
<div class="abs dots"><i class="on"></i><i></i><i></i><i></i></div>

<h2 class="abs cta-title">READY TO BUILD YOUR NEXT<br>SELF STORAGE PROJECT?</h2>
<p class="abs cta-sub">Let’s talk</p>
<a class="abs btn-arrow cta-btn" style="padding-left:30px">CONTACT US
  <svg width="34" height="24" viewBox="0 0 26 20"><path d="M2 7h12V2l10 8-10 8v-5H2z" fill="none" stroke="#fff" stroke-width="2"/></svg></a>

<svg class="abs" width="1200" height="560" style="left:0;top:3627px">
  <polygon points="0,30 600,180 1200,30 1200,560 0,560" fill="var(--dark)"/>
</svg>

<footer>
  <div class="abs footer-head" style="left:227px;top:3875px">QUICK LINKS</div>
  <ul class="abs links" style="left:227px;top:3940px">
    <li>Home</li><li>About Us</li><li>Services</li><li>Featured Projects</li><li>Contact Us</li>
  </ul>
  <div class="abs footer-mark"></div>
  <div class="abs footer-brand">Keystone Vault Depot Services</div>
  <div class="abs footer-head" style="left:813px;top:3875px">CONTACT US</div>
  <div class="abs" style="left:813px;top:3946px">
    <div class="contact-row"><span class="ico"><svg width="14" height="14" viewBox="0 0 24 24"><path d="M6 2l4 4-2 3c1 3 4 6 7 7l3-2 4 4-3 4C10 21 3 14 2 5z" fill="none" stroke="#2baadf" stroke-width="2"/></svg></span><span>CALL US<br>0123 456 789</span></div>
    <div class="contact-row"><span class="ico"><svg width="14" height="12" viewBox="0 0 24 18"><rect x="1" y="1" width="22" height="16" fill="none" stroke="#2baadf" stroke-width="2"/><path d="M1 1l11 9 11-9" fill="none" stroke="#2baadf" stroke-width="2"/></svg></span><span>EMAIL US<br>info@webname.com</span></div>
    <div class="contact-row"><span class="ico"><svg width="12" height="16" viewBox="0 0 18 24"><path d="M9 23S1 13 1 8a8 8 0 0 1 16 0c0 5-8 15-8 15z" fill="none" stroke="#2baadf" stroke-width="2"/><circle cx="9" cy="8" r="3" fill="#2baadf"/></svg></span><span>Address Line goes here,<br>Country Name, 4231</span></div>
  </div>
  <div class="abs rule"></div>
  <p class="abs copy">Copyright © 2025 All Rights Reserved By Company name</p>
</footer>

</body>
</html>
```